HollowPine Ventures Inc. Business Card Design

My business is custom renovations and homes.I would need to have a new business logo created to go along with my company name. The business card should be of a modern style as this is the market I am focused on. I would need my contact information and website posted on the card. I would also like to list a few of the tasks I conduct on the card (such as: Renovations, Additions, Repairs, New Homes, Design, Consultations). On the reverse of the card I currently have just my logo and my motto, "Shaping A Bold Path". However, I am open to completely changing everything as I am starting a new year and would like to excel further. Any new ideas and suggestions are always welcomed. Thank you.

Target Market(s)

Upscale residential and commercial renovations and builds

Industry/Entity Type

Business

Contact Information for Business Card

I would like the design to be able to be laser cut or burnt onto a wooden business card. I will be creating one option of cards for really loyal customers (wooden) and a second option for the everyday customer (paper).

Font styles to use
Other font styles liked:
• Calibri / anything of mordern taste

Colors
f37122
5c5c5c
474747
ffffff

Requirements
Must have
• I would like the colours of my business to be a sharp orange and grey. I believe this will symbolize a modern style. I am open to other suggestions if this is not suitable for the designers tastes. My contact info as follows:
• Will Marsh
• President
• HollowPine Ventures Inc.
• 555-214-3987
• will@hollowpineventures.example
• I would like my website (currently under construction) hollowpineventures.example on the card aswell.
Nice to have
• Along with a modern logo representing HollowPine, I would like something on the card besides the logo and contact information. Perhaps a small background design. I feel it may be nice to have my services listed on the card (in smaller font on the bottom) Renovations, Additions, Repairs, Design, Consultations.
Should not have
• The business card should not have too many different colors. Should not have rounded corners.

```html
<!DOCTYPE html>
<html lang="en">
<head>
<meta charset="utf-8">
<title>HollowPine Ventures Inc. – Business Card</title>
<link rel="stylesheet" href="https://fonts.googleapis.com/css2?family=Open+Sans:wght@400;600;700&display=swap">
<style>
  :root {
    --orange: #f37122;
    --grey: #5c5c5c;
    --charcoal: #474747;
    --dark: #25282b;
    --white: #ffffff;
    --paper: #f2f2f2;
    --backdrop: #d9d4cc;
  }
  * { margin: 0; padding: 0; box-sizing: border-box; }
  html, body {
    width: 1200px; height: 780px; overflow: hidden;
    background: var(--backdrop);
    font-family: "Open Sans", Calibri, sans-serif;
  }
  .canvas { position: relative; width: 1200px; height: 780px; }
  .card {
    position: absolute; width: 560px; height: 320px;
    background: linear-gradient(160deg, var(--white), var(--paper));
    box-shadow: 0 10px 28px rgba(0,0,0,.28);
    overflow: hidden;
  }
  .card-front { left: 50px; top: 60px; }
  .card-back { left: 590px; top: 400px; }
  .card-shape { position: absolute; inset: 0; width: 100%; height: 100%; }

  /* front */
  .company-name {
    position: absolute; left: 34px; top: 36px;
    font-size: 31px; font-weight: 600; color: var(--charcoal);
    letter-spacing: -0.3px; white-space: nowrap;
  }
  .tagline {
    position: absolute; left: 37px; top: 84px;
    font-size: 13px; font-weight: 600; color: var(--grey);
    letter-spacing: 4px; white-space: nowrap;
  }
  .person { position: absolute; left: 40px; top: 220px; text-align: right; width: 150px; }
  .person-name { font-size: 22px; font-weight: 600; color: var(--white); line-height: 1.1; }
  .person-title { font-size: 15px; font-weight: 600; color: var(--orange); }
  .divider { position: absolute; left: 204px; top: 216px; width: 1px; height: 56px; background: #6a6d70; }
  .contact { position: absolute; left: 218px; top: 218px; list-style: none; }
  .contact li {
    display: flex; align-items: center; gap: 7px;
    font-size: 13px; color: var(--white); line-height: 25px; white-space: nowrap;
  }
  .contact svg { width: 13px; height: 13px; fill: var(--orange); }
  .website {
    position: absolute; left: 140px; bottom: 7px;
    font-size: 14px; font-weight: 600; color: var(--white);
  }

  /* back */
  .brand { position: absolute; right: 34px; top: 60px; text-align: right; }
  .brand-mark-row { display: flex; align-items: center; justify-content: flex-end; gap: 12px; }
  .brand-square { width: 26px; height: 26px; background: var(--orange); }
  .brand-name { font-size: 30px; font-weight: 600; color: var(--charcoal); white-space: nowrap; }
  .brand-tagline {
    margin-top: 6px; font-size: 13px; font-weight: 600; color: var(--grey);
    letter-spacing: 4px;
  }
  .services {
    position: absolute; right: 34px; top: 200px; text-align: right;
    font-size: 14px; color: var(--grey); line-height: 24px;
  }
  .services .sep { color: var(--orange); padding: 0 5px; }
</style>
</head>
<body>
<main class="canvas">

  <section class="card card-front" aria-label="Business card front">
    <svg class="card-shape" viewBox="0 0 560 320" preserveAspectRatio="none" aria-hidden="true">
      <path d="M0,200 C225,190 430,120 548,0" fill="none" stroke="var(--orange)" stroke-width="4"/>
      <path d="M0,210 C230,200 450,130 560,20 L560,320 L0,320 Z" fill="var(--dark)"/>
      <rect x="0" y="288" width="560" height="32" fill="var(--orange)"/>
    </svg>
    <div class="company-name">HollowPine Ventures Inc.</div>
    <div class="tagline">Shaping A Bold Path</div>
    <div class="person">
      <div class="person-name">Will Marsh</div>
      <div class="person-title">President</div>
    </div>
    <div class="divider"></div>
    <ul class="contact">
      <li>
        <svg viewBox="0 0 24 24" aria-hidden="true"><path d="M6.6 10.8a15 15 0 0 0 6.6 6.6l2.2-2.2a1 1 0 0 1 1-.25 11.4 11.4 0 0 0 3.6.57 1 1 0 0 1 1 1V20a1 1 0 0 1-1 1A17 17 0 0 1 3 4a1 1 0 0 1 1-1h3.5a1 1 0 0 1 1 1c0 1.25.2 2.45.57 3.57a1 1 0 0 1-.25 1z"/></svg>
        555-214-3987
      </li>
      <li>
        <svg viewBox="0 0 24 24" aria-hidden="true"><path d="M2 5h20v14H2zm2 2v.5l8 5 8-5V7zm0 2.8V17h16V9.8l-8 5z"/></svg>
        will@hollowpineventures.example
      </li>
    </ul>
    <div class="website">hollowpineventures.example</div>
  </section>

  <section class="card card-back" aria-label="Business card back">
    <svg class="card-shape" viewBox="0 0 560 320" preserveAspectRatio="none" aria-hidden="true">
      <path d="M58,0 C70,130 190,260 400,320" fill="none" stroke="var(--orange)" stroke-width="4"/>
      <path d="M0,0 L48,0 C58,135 180,268 380,320 L0,320 Z" fill="var(--dark)"/>
    </svg>
    <div class="brand">
      <div class="brand-mark-row">
        <span class="brand-square"></span>
        <span class="brand-name">HollowPine Ventures Inc.</span>
      </div>
      <div class="brand-tagline">Shaping A Bold Path</div>
    </div>
    <div class="services">
      Renovations<span class="sep">|</span>Additions<span class="sep">|</span>Repairs<span class="sep">|</span>Design<br>
      Consultations
    </div>
  </section>

</main>
</body>
</html>
```